Business Card Design

My business will be called TB Carpentry & Renovations. I am a liscenced carpentar who specialises in renovations/alterations/refurbishments and maintenance. I have experience in all types of Carpentry tho. I also have experience in tiling, painting and concrete which obviously gives me an edge in the refurbishment market for building. But i am not liscenced in these trades. I pride myself on being an honest and very reliable. There are alot of tradesman where i live who are not reliable so i really want to let the community know they can trust me and that i am willing to do all types of work.
I would like to see design and is not over the top but uses earthy/modern colours which presents a down to earth message.

I would really like to communicate diversity, reliabilty and quality work.

I have attached a couple of concepts i have come up with PrintNest, These may aid you.
Updates

Industry/Entity Type

Painting

Contact Information for Business Card

Name: Dean Holloway
Email: dean.holl@examplemail.net
Ph: 0418552916

Requirements
Must have
• Licence No: 581937K

```html
<!DOCTYPE html>
<html lang="en">
<head>
<meta charset="UTF-8">
<title>TB Carpentry &amp; Renovations – Business Card</title>
<link rel="stylesheet" href="https://fonts.googleapis.com/css2?family=Cinzel+Decorative:wght@700&family=Cinzel:wght@400&family=Cormorant+SC:wght@500&display=swap">
<style>
  :root {
    --wood-dark: #1e0f08;
    --wood-mid: #2e1a10;
    --wood-light: #3a2114;
    --copper: #c48a63;
    --copper-light: #e0ad85;
    --engrave-shadow: rgba(0, 0, 0, 0.85);
    --engrave-highlight: rgba(255, 210, 170, 0.18);
  }
  * { margin: 0; padding: 0; box-sizing: border-box; }
  html, body {
    width: 1200px;
    height: 741px;
    overflow: hidden;
    background: var(--wood-dark);
  }
  .card {
    position: relative;
    width: 1200px;
    height: 741px;
    overflow: hidden;
    background:
      linear-gradient(90deg,
        rgba(0,0,0,0.25) 0%, rgba(0,0,0,0) 8%, rgba(0,0,0,0.1) 20%,
        rgba(0,0,0,0) 34%, rgba(0,0,0,0.2) 48%, rgba(0,0,0,0) 60%,
        rgba(0,0,0,0.12) 74%, rgba(0,0,0,0) 86%, rgba(0,0,0,0.22) 100%),
      radial-gradient(ellipse at 50% 45%, var(--wood-light) 0%, var(--wood-mid) 55%, var(--wood-dark) 100%);
  }
  .engraved {
    position: absolute;
    color: var(--copper);
    text-shadow:
      -1px -1px 1px var(--engrave-shadow),
      1px 1px 1px var(--engrave-highlight),
      2px 2px 3px rgba(0,0,0,0.5);
    white-space: nowrap;
  }
  .business-name {
    left: 0;
    width: 1200px;
    top: 124px;
    text-align: center;
    font-family: "Cinzel Decorative", serif;
    font-weight: 700;
    font-size: 54px;
    letter-spacing: 5px;
    color: var(--copper-light);
  }
  .owner-name {
    left: 88px;
    top: 336px;
    font-family: "Cinzel", serif;
    font-size: 44px;
    letter-spacing: 2px;
  }
  .services { list-style: none; }
  .service {
    left: 88px;
    font-family: "Cormorant SC", serif;
    font-weight: 500;
    font-size: 35px;
    letter-spacing: 1.5px;
  }
  .service:nth-child(1) { top: 410px; }
  .service:nth-child(2) { top: 464px; }
  .service:nth-child(3) { top: 518px; }
  .service:nth-child(4) { top: 570px; }
  .service:nth-child(5) { top: 624px; }
  .contact {
    font-family: "Cormorant SC", serif;
    font-weight: 500;
    font-size: 29px;
    letter-spacing: 1.5px;
    text-transform: lowercase;
  }
  .contact-email { right: 82px; top: 574px; }
  .contact-phone { left: 788px; width: 300px; text-align: center; top: 626px; }
</style>
</head>
<body>
  <main class="card">
    <h1 class="engraved business-name">TB Carpentry &amp; Renovations</h1>
    <p class="engraved owner-name">Dean Holloway</p>
    <ul class="services">
      <li class="engraved service">Carpentry &amp; All Building Sevices</li>
      <li class="engraved service">Renovations</li>
      <li class="engraved service">Maintainence</li>
      <li class="engraved service">General Repairs</li>
      <li class="engraved service">Liscence No. 581937K</li>
    </ul>
    <p class="engraved contact contact-email">dean.holl@examplemail.net</p>
    <p class="engraved contact contact-phone">0418 552 916</p>
  </main>
</body>
</html>
```